Flyer Design Project

Need a DL Size flyer (2 sided) for letter box marketing for our website www.brightwardsecure.com.au
Updates

Project Deadline Extended
Reason: Thank you for submitting the designs. We like few of the designs and will request those designers to changes few things to make it more suitable for us. Because of holidays need to extend the deadlines. Thank you.

Industry/Entity Type

Marketing

```html
<!DOCTYPE html>
<html lang="en">
<head>
<meta charset="utf-8">
<title>Brightward Secure – CCTV System Specialist</title>
<link rel="stylesheet" href="https://fonts.googleapis.com/css2?family=Arimo:wght@400;700&display=swap">
<style>
  :root {
    --navy-deep: #1a2a66;
    --blue-top: #1d4f9e;
    --blue-light: #3f7fd0;
    --blue-lower: #1b5cb4;
    --gold: #f6b816;
    --gold-deep: #e9a800;
    --white: #ffffff;
    --footer-text: #e6ecf7;
    --icon-blue: #3fb2e6;
    --camera-shell: #e9ebee;
    --camera-shade: #b9bfc8;
  }
  * { margin: 0; padding: 0; box-sizing: border-box; }
  html, body { width: 1200px; height: 566px; overflow: hidden; background: var(--navy-deep); }
  .flyer {
    position: relative;
    width: 1200px;
    height: 566px;
    overflow: hidden;
    font-family: "Arimo", Arial, sans-serif;
    color: var(--white);
    background:
      linear-gradient(115deg, rgba(255,255,255,0) 40%, rgba(120,170,235,0.35) 62%, rgba(255,255,255,0) 80%),
      linear-gradient(180deg, var(--blue-top) 0%, #2560b4 45%, var(--blue-lower) 100%);
  }
  .skyline {
    position: absolute;
    left: 0; top: 0;
    width: 1200px; height: 490px;
    background: linear-gradient(160deg, rgba(255,255,255,0.05) 20%, rgba(160,200,245,0.18) 55%, rgba(255,255,255,0.04) 85%);
  }
  .brand-band {
    position: absolute;
    left: 0; top: 256px;
    width: 1200px; height: 72px;
    background: linear-gradient(90deg, var(--gold-deep) 0%, var(--gold) 45%, rgba(246,184,22,0.85) 70%, rgba(246,184,22,0.55) 100%);
  }
  .headline {
    position: absolute;
    left: 58px; top: 58px;
    font-size: 76px;
    font-weight: 700;
    color: var(--gold);
    letter-spacing: 0.5px;
    white-space: nowrap;
  }
  .tagline {
    position: absolute;
    left: 58px; top: 170px;
    font-size: 54px;
    font-weight: 700;
    white-space: nowrap;
  }
  .contact-line {
    position: absolute;
    left: 58px; top: 274px;
    font-size: 34px;
    font-weight: 700;
    white-space: nowrap;
  }
  .contact-line .divider { margin: 0 8px; }
  .benefits {
    position: absolute;
    left: 62px; top: 364px;
    display: grid;
    grid-template-columns: 395px auto;
    row-gap: 10px;
    list-style: none;
    font-size: 24px;
    font-weight: 700;
  }
  .benefits li::before { content: "•"; margin-right: 10px; }
  .camera-photo {
    position: absolute;
    left: 830px; top: 62px;
    width: 330px; height: 420px;
  }
  .footer {
    position: absolute;
    left: 0; top: 490px;
    width: 1200px; height: 76px;
    background: var(--navy-deep);
    display: flex;
    align-items: center;
    padding-left: 61px;
  }
  .footer .social-square {
    width: 38px; height: 38px;
    border-radius: 6px;
    background: var(--icon-blue);
    margin-right: 24px;
    flex: none;
  }
  .footer .follow-text {
    font-size: 23px;
    color: var(--footer-text);
    white-space: nowrap;
  }
</style>
</head>
<body>
  <main class="flyer">
    <div class="skyline" role="img" aria-label="Faint background photo of glass office towers"></div>
    <div class="brand-band"></div>

    <h1 class="headline">Brightward Secure</h1>
    <p class="tagline">CCTV System Specialist</p>
    <p class="contact-line">www.brightwardsecure.com.au<span class="divider">|</span>02 5550 1834</p>

    <ul class="benefits">
      <li>High quality hardware</li>
      <li>1 year full warranty</li>
      <li>100% customer satisfaction</li>
      <li>14 days money back guarantee</li>
    </ul>

    <svg class="camera-photo" viewBox="0 0 330 420" role="img" aria-label="Photo of a white dome security camera">
      <defs>
        <radialGradient id="shellTone" cx="40%" cy="35%" r="75%">
          <stop offset="0%" stop-color="#f7f8fa"/>
          <stop offset="70%" stop-color="var(--camera-shell)"/>
          <stop offset="100%" stop-color="var(--camera-shade)"/>
        </radialGradient>
      </defs>
      <path d="M30 0 H300 V150 C300 330 250 420 165 420 C80 420 30 330 30 150 Z" fill="url(#shellTone)"/>
    </svg>

    <footer class="footer">
      <span class="social-square" aria-hidden="true"></span>
      <p class="follow-text">Follow us on Chirpline to receive updates regarding network issues, discounts and more.</p>
    </footer>
  </main>
</body>
</html>
```